I need a business card and letterhead design for a company that provides labor for moves.
Please use existing logo.
Great designs. I really like #5 but for practical and economic reasons, I will choose #3. However we are a traveling moving company. We have no location for clients to visit. Can you reproduce #3, without an address?
The project form requires one, but in my case not needed.

```html
<!DOCTYPE html>
<html lang="en">
<head>
<meta charset="utf-8">
<title>Kestrel4ox Business Card</title>
<link href="https://fonts.googleapis.com/css2?family=Questrial&display=swap" rel="stylesheet">
<style>
  :root {
    --page-bg: #e4e4e4;
    --card-white: #ffffff;
    --card-black: #1b1b1b;
    --brand-red: #e3232c;
    --stripe-pink: #f3a3a6;
    --text-light: #f2f2f2;
    --text-muted: #a9a9a9;
  }
  * { margin: 0; padding: 0; box-sizing: border-box; }
  html, body {
    width: 1200px; height: 901px; overflow: hidden;
    background: var(--page-bg);
    font-family: "Questrial", "Century Gothic", sans-serif;
  }
  .stage {
    width: 1200px; height: 901px;
    display: flex; align-items: center; justify-content: center; gap: 60px;
  }
  .card {
    width: 500px; height: 286px; position: relative; overflow: hidden;
    box-shadow: 0 10px 28px rgba(0,0,0,0.18);
  }
  .card-back {
    background: var(--card-black);
    display: flex; align-items: center; justify-content: center;
  }
  .brand-name {
    font-size: 54px; letter-spacing: 1px; text-transform: uppercase; line-height: 1;
  }
  .card-back .brand-name { color: var(--card-white); }
  .card-front { background: var(--card-white); }
  .front-brand {
    position: absolute; top: 0; left: 0; right: 0; height: 148px;
    display: flex; align-items: center; justify-content: center;
  }
  .card-front .brand-name { color: var(--brand-red); }
  .stripe {
    position: absolute; left: 0; right: 0; height: 3px;
    background: repeating-linear-gradient(90deg, var(--brand-red) 0 6px, var(--stripe-pink) 6px 9px);
  }
  .stripe-top { top: 150px; }
  .stripe-bottom { top: 247px; }
  .contact-band {
    position: absolute; top: 156px; left: 0; right: 0; height: 88px;
    background: var(--card-black);
    display: flex; align-items: center;
  }
  .person { width: 50%; padding-right: 14px; text-align: right; }
  .person-name { color: var(--text-light); font-size: 18px; }
  .person-role { color: var(--text-muted); font-size: 8px; margin-top: 3px; letter-spacing: 0.5px; }
  .band-divider { width: 1px; height: 54px; background: var(--text-muted); }
  .contact-list { list-style: none; padding-left: 14px; }
  .contact-list li {
    color: var(--text-light); font-size: 8.5px; line-height: 15px;
    display: flex; align-items: center; gap: 6px;
  }
  .contact-list svg { width: 8px; height: 8px; fill: var(--text-light); }
  .website {
    position: absolute; bottom: 14px; left: 0; right: 0; text-align: center;
    color: var(--brand-red); font-size: 9px; letter-spacing: 1px;
  }
</style>
</head>
<body>
<main class="stage">
  <section class="card card-back">
    <span class="brand-name">Kestrel4ox</span>
  </section>

  <section class="card card-front">
    <div class="front-brand"><span class="brand-name">Kestrel4ox</span></div>
    <div class="stripe stripe-top"></div>
    <div class="contact-band">
      <div class="person">
        <p class="person-name">Marco Ellison</p>
        <p class="person-role">Move Coordinator</p>
      </div>
      <div class="band-divider"></div>
      <ul class="contact-list">
        <li><svg viewBox="0 0 10 10"><path d="M2 0h2l1 3-1.5 1a6 6 0 0 0 2.5 2.5L7 5l3 1v2a2 2 0 0 1-2 2A8 8 0 0 1 0 2a2 2 0 0 1 2-2z"/></svg>555 210 4870</li>
        <li><svg viewBox="0 0 10 10"><rect x="2.5" y="0" width="5" height="10" rx="1"/></svg>555 318 2946</li>
        <li><svg viewBox="0 0 10 10"><path d="M0 2h10v6H0z M0 2l5 3.5L10 2" /></svg>crew@kestrel4ox.com</li>
      </ul>
    </div>
    <div class="stripe stripe-bottom"></div>
    <p class="website">www.kestrel4ox.com</p>
  </section>
</main>
</body>
</html>
```